Redesign of 2 real estate websites!

We need a redesign of our two real estate websites. These websites offer detailed information on the two real estates and need a modern fresh up.
Both websites should have the same design type, so you can see that they belong together, yet they should be in different colors. There is no logo to these pages, so the headlines can be integreated into the designs.
http://www.lindqvar-villa.de
http://www.osmund-lindqvar-haus.de/

```html
<!DOCTYPE html>
<html lang="de">
<head>
<meta charset="utf-8">
<title>Osmund-Lindqvar-Haus</title>
<link rel="stylesheet" href="https://fonts.googleapis.com/css2?family=Open+Sans:ital,wght@0,300;0,400;0,600;1,400&display=swap">
<style>
:root{
  --orange:#c46200;
  --orange-light:#dd7d1f;
  --peach:#fdd6a6;
  --text:#333;
  --muted:#666;
  --line:#e2e2e2;
  --white:#fff;
}
*{box-sizing:border-box;margin:0;padding:0}
html,body{width:1200px;height:1182px;overflow:hidden;background:var(--white);font-family:"Open Sans",Arial,sans-serif;color:var(--text)}
.page{position:relative;width:1200px;height:1182px}
.site-title{position:absolute;left:222px;top:34px;font-size:22px;font-weight:400;color:var(--orange-light);letter-spacing:-.3px}
.other-site{position:absolute;left:414px;top:69px;font-size:12.5px;color:#222;display:flex;align-items:center;gap:6px}
.contact{position:absolute;right:216px;top:37px;display:flex;align-items:center;gap:4px;font-size:18px;color:#444;white-space:nowrap}
.social{width:21px;height:21px;border-radius:50%;border:2px solid #2f8fd0}
.contact span{margin-left:4px}
.header-rule{position:absolute;left:0;top:111px;width:1200px;height:1px;background:var(--line)}
.main-nav{position:absolute;left:215px;top:111px;width:176px;height:490px;background:var(--orange);border-bottom-right-radius:40px;box-shadow:0 4px 6px rgba(0,0,0,.08);z-index:2}
.main-nav ul{list-style:none;padding-top:34px}
.main-nav li{position:relative;height:28.5px;line-height:28.5px;padding-left:29px;font-size:14px;color:var(--white);font-weight:400}
.main-nav li.home{border-bottom:1px solid rgba(255,255,255,.25)}
.main-nav li svg{position:absolute;left:141px;top:10px}
.hero{position:absolute;left:391px;top:111px;width:593px;height:490px;background:linear-gradient(180deg,#dfe2e4 0%,#d9c3a4 30%,#b98d6a 55%,#7e7570 72%,#6d6a68 100%)}
.hero-caption{position:absolute;left:27px;top:370px;width:300px;font-size:16px;line-height:22px;color:var(--white);text-shadow:0 1px 2px rgba(0,0,0,.35)}
.cta{position:absolute;left:27px;top:425px;width:144px;height:33px;border-radius:17px;background:var(--orange);color:var(--white);font-size:15px;text-align:center;line-height:33px}
.dots{position:absolute;left:528px;top:461px;display:flex;gap:2px}
.dots i{width:10px;height:10px;border-radius:50%;background:var(--white)}
.dots i.active{background:#111}
.card{position:absolute;top:664px;width:240px;height:378px;border:1px solid var(--line);box-shadow:0 1px 3px rgba(0,0,0,.06);text-align:center}
.card h2{margin-top:24px;font-size:24px;font-weight:400;color:var(--orange)}
.card .media{position:relative;margin:14px auto 0;width:201px;height:160px}
.card p{font-size:14.4px;line-height:18px;color:var(--muted);margin-top:20px;padding:0 14px}
.about p{padding:0 4px;letter-spacing:-.15px;white-space:nowrap}
.btn{position:absolute;left:75px;top:321px;width:88px;height:18px;background:var(--orange);color:var(--white);font-size:11px;line-height:18px;text-align:center}
.about{left:216px}
.about .media{background:linear-gradient(135deg,#cfd6dc 0%,#e9ecee 45%,#b7a89a 70%,#3b3b3b 100%)}
.play{position:absolute;left:74px;top:58px}
.gallery{left:482px}
.gallery .media{background:linear-gradient(90deg,#7a7270 0%,#c7c2bd 30%,#efece6 55%,#d8a24a 75%,#c68a2b 100%)}
.gallery .arrow{position:absolute;top:70px}
.gallery .subtitle{margin-top:20px;font-size:14.4px;color:var(--orange)}
.gallery .subtitle + p{margin-top:2px}
.testimonials{left:745px;width:239px;background:var(--peach);border:none;text-align:left}
.testimonials h2{text-align:center}
.testimonials hr{border:none;height:1px;background:rgba(255,255,255,.6);margin:11px 19px 0}
.quote{padding:0 18px 0 19px;margin-top:18px;font-size:11.4px;line-height:15px;color:#111}
.quote + .quote{margin-top:22px}
.quote time{display:block;text-align:right;font-style:italic;font-size:11px;margin-top:2px;padding-right:17px}
.testimonials .btn{left:19px}
.footer-nav{position:absolute;left:0;top:1092px;width:1200px;text-align:center;font-size:11px;color:#555}
.copyright{position:absolute;left:0;top:1118px;width:1200px;text-align:center;font-size:11px;color:#555}
</style>
</head>
<body>
<div class="page">
  <header>
    <h1 class="site-title">OSMUND-LINDQVAR-HAUS!</h1>
    <div class="other-site">Other site
      <svg width="12" height="12" viewBox="0 0 12 12"><circle cx="6" cy="6" r="6" fill="#111"/><path d="M3.5 5l2.5 2.5L8.5 5" stroke="#fff" stroke-width="1.5" fill="none"/></svg>
    </div>
    <div class="contact">
      <i class="social"></i><i class="social" style="border-color:#25a9e0"></i>
      <span>Toll Free : 1800 555 019</span>
    </div>
  </header>
  <div class="header-rule"></div>

  <nav class="main-nav">
    <ul>
      <li class="home">Home</li>
      <li>Stadt Valdenau</li>
      <li>Das Haus<svg width="8" height="8" viewBox="0 0 8 8"><circle cx="4" cy="4" r="4" fill="#fff"/><path d="M3 2.3L4.8 4 3 5.7" stroke="#c46200" stroke-width="1.2" fill="none"/></svg></li>
      <li>Wohnungen<svg width="8" height="8" viewBox="0 0 8 8"><circle cx="4" cy="4" r="4" fill="#fff"/><path d="M3 2.3L4.8 4 3 5.7" stroke="#c46200" stroke-width="1.2" fill="none"/></svg></li>
      <li>Wohnqualiät</li>
      <li>Büros<svg width="8" height="8" viewBox="0 0 8 8"><circle cx="4" cy="4" r="4" fill="#fff"/><path d="M3 2.3L4.8 4 3 5.7" stroke="#c46200" stroke-width="1.2" fill="none"/></svg></li>
      <li>Klimaanlagen</li>
      <li>Gewerbl. Mieter<svg width="8" height="8" viewBox="0 0 8 8"><circle cx="4" cy="4" r="4" fill="#fff"/><path d="M3 2.3L4.8 4 3 5.7" stroke="#c46200" stroke-width="1.2" fill="none"/></svg></li>
      <li>Links / Anfahrt</li>
      <li>Kontakt</li>
      <li>Impressum</li>
      <li>Vermietung</li>
    </ul>
  </nav>

  <section class="hero" role="img" aria-label="Photo of the house and the town square with historic town hall">
    <p class="hero-caption">Lorem ipsum dolor sit amet, adipiscing elit. Sed dolor non augue pretium.</p>
    <div class="cta">Call to Action</div>
    <div class="dots"><i class="active"></i><i></i><i></i><i></i></div>
  </section>

  <section class="card about">
    <h2>About Us</h2>
    <div class="media" role="img" aria-label="Video still of a bright office interior">
      <svg class="play" width="52" height="52" viewBox="0 0 52 52"><circle cx="26" cy="26" r="24" fill="#fff" stroke="#111" stroke-width="3"/><path d="M20 16l15 10-15 10z" fill="#111"/></svg>
    </div>
    <p>Im Osmund-Lindqvar-Haus<br>können sehr hochwertige Büros<br>von 18 bis 400 qm Fläche</p>
    <div class="btn">Click Here</div>
  </section>

  <section class="card gallery">
    <h2>Our Gallery</h2>
    <div class="media" role="img" aria-label="Photo of a hallway with a yellow wall sculpture">
      <svg class="arrow" style="left:14px" width="18" height="18" viewBox="0 0 18 18"><circle cx="9" cy="9" r="8" fill="none" stroke="#888" stroke-width="1.2"/><path d="M10.5 5.5L7 9l3.5 3.5z" fill="#888"/></svg>
      <svg class="arrow" style="left:171px" width="18" height="18" viewBox="0 0 18 18"><circle cx="9" cy="9" r="8" fill="none" stroke="#666" stroke-width="1.2"/><path d="M7.5 5.5L11 9l-3.5 3.5z" fill="#666"/></svg>
    </div>
    <div class="subtitle">Plastik des Künstlers</div>
    <p>Lorem ipsum dolor sit , consectetur adipiscing elit.</p>
    <div class="btn">Click Here</div>
  </section>

  <section class="card testimonials">
    <h2>Testimonials</h2>
    <hr>
    <div class="quote">Lorem ipsum dolor sit , adipiscing elit. In fermentum dolor non fermentum ipsum consectetur<time>23 April, 2014</time></div>
    <div class="quote">Lorem ipsum dolor sit , adipiscing elit. In fermentum dolor non fermentum ipsum consectetur<time>23 April, 2014</time></div>
    <div class="quote">Lorem ipsum dolor sit , adipiscing elit. In fermentum dolor non fermentum ipsum consectetur<time>23 April, 2014</time></div>
    <div class="btn">Click Here</div>
  </section>

  <footer>
    <div class="footer-nav">Home &nbsp;/&nbsp; About us &nbsp;/&nbsp; Gallery &nbsp;/&nbsp; Contact us &nbsp;/&nbsp; Login &nbsp;/&nbsp; Terms</div>
    <div class="copyright">Copyright © 2014</div>
  </footer>
</div>
</body>
</html>
```